Business Card Design

Name of company: Brisk Property Maintenance.
We are a new start up business.
The company is involved in general property maintenance around residential properties and high rise apartment buildings.
We carry out all types of property maintenance such as:
*Handyman work
*Plumbing
*Painting
*Electrical
*Window cleaning
*Gardens / Landscaping

Target Market(s)

*Real Estate Agents
*Body corporate managers
*Private apartment owners

Industry/Entity Type

Property Maintenance

Requirements
Must have
• Name: Dean Malloy
Address: PO Box 3862
Carrow Hill Crossing
NSW 2417
Phone: 0431 962 305
Email: dean@briskpropertymaintenance
Website: www.briskpropertymaintenance.example.au
Nice to have
• We don't have any corporate logo so you can design what you think is appropriate

```html
<!DOCTYPE html>
<html lang="en">
<head>
<meta charset="utf-8">
<title>Brisk Property Maintenance – Business Card</title>
<link rel="stylesheet" href="https://fonts.googleapis.com/css2?family=Arimo:wght@400;700&display=swap">
<style>
  :root {
    --brand-blue: #1f47a0;
    --ink: #2b2b2b;
    --muted: #555555;
    --rule: #9aa6c4;
    --card: #ffffff;
    --backdrop: #e9e9ea;
  }
  * { margin: 0; padding: 0; box-sizing: border-box; }
  html, body { width: 1200px; height: 864px; overflow: hidden; }
  body {
    background: var(--backdrop);
    font-family: "Arimo", Arial, sans-serif;
    color: var(--ink);
    position: relative;
  }
  .business-card {
    position: absolute;
    left: 120px; top: 152px;
    width: 960px; height: 560px;
    background: var(--card);
    box-shadow: 0 6px 24px rgba(0,0,0,0.12);
  }
  .brand {
    position: absolute;
    left: 60px; top: 250px;
    width: 370px;
    display: flex; align-items: center; gap: 12px;
  }
  .brand-mark {
    width: 16px; height: 16px;
    background: var(--brand-blue);
    flex: none;
  }
  .brand-name {
    font-size: 28px; font-weight: 700;
    color: var(--brand-blue);
    line-height: 1.15;
  }
  .divider {
    position: absolute;
    left: 470px; top: 60px;
    width: 2px; height: 345px;
    background: var(--brand-blue);
  }
  .contact {
    position: absolute;
    left: 505px; top: 78px;
    width: 440px;
  }
  .person-name {
    font-size: 34px; font-weight: 700;
    color: var(--brand-blue);
    letter-spacing: 0.5px;
  }
  .person-role {
    font-size: 18px; color: var(--muted);
    margin-top: 4px;
  }
  .contact-list { list-style: none; margin-top: 58px; }
  .contact-list li {
    display: flex; align-items: center; gap: 12px;
    font-size: 19px; line-height: 30px;
    white-space: nowrap;
  }
  .contact-list svg { width: 20px; height: 20px; flex: none; fill: var(--brand-blue); }
  .services {
    position: absolute;
    left: 0; right: 0; top: 432px;
    text-align: center;
    color: var(--brand-blue);
    font-size: 22px;
    line-height: 30px;
  }
  .services span + span { border-left: 1.5px solid var(--rule); padding-left: 8px; margin-left: 6px; }
</style>
</head>
<body>
  <div class="business-card">
    <div class="brand">
      <span class="brand-mark"></span>
      <span class="brand-name">Brisk Property Maintenance</span>
    </div>

    <div class="divider"></div>

    <div class="contact">
      <div class="person-name">DEAN MALLOY</div>
      <div class="person-role">Maneger</div>
      <ul class="contact-list">
        <li>
          <svg viewBox="0 0 20 20" aria-hidden="true"><circle cx="10" cy="6" r="4.5"/><path d="M1 19c0-5 4-8 9-8s9 3 9 8z"/></svg>
          0431 962 305
        </li>
        <li>
          <svg viewBox="0 0 20 20" aria-hidden="true"><path d="M1 4h18v12H1z"/><path d="M1 4l9 7 9-7" fill="none" stroke="#fff" stroke-width="1.6"/></svg>
          dean@briskpropertymaintenance.example.au
        </li>
        <li>
          <svg viewBox="0 0 20 20" aria-hidden="true"><circle cx="10" cy="10" r="9"/><path d="M1 10h18M10 1c-4 5-4 13 0 18M10 1c4 5 4 13 0 18" fill="none" stroke="#fff" stroke-width="1.3"/></svg>
          www.briskpropertymaintenance.example.au
        </li>
        <li class="address">PO Box 3862 Carrow Hill Crossing NSW 2417</li>
      </ul>
    </div>

    <div class="services">
      <div><span>Handyman work</span><span>Plumbing</span><span>Painting</span><span>Electrical</span><span>Window cleaning</span></div>
      <div>Gardens / Landscaping</div>
    </div>
  </div>
</body>
</html>
```